Webdesign für Reisebüro
Zielgruppe
Reisebüro - wir haben uns vor 20 Jahren auf Reisen nach Asien spezialisiert aber inzwischen ist unsere Kernkompetenz das individuelle Arrangieren von Fernreisen in alle Welt. Jedoch decken wir auch das komplette touristische Portfolio ab was natürlich auch nicht zu kurz kommen darf. Unsere Zielgruppe liegt tatsächlich zwischen 20—70
Aufgabenstellung
Wir bezeichnen uns als das besondere Reisebüro weil wir als Menschen besonders sind. Wir lieben es zu begeistern und das gelingt uns so gut dass wir seit bestimmt 15 Jahren komplett ohne Werbung auskommen und nur von Mundpropaganda leben. Das Design soll genau dieses Besondere zum Ausdruck bringen. Soll keine „klassische“ Reisebüroseite sein auf der man selbst Reisen suchen Und buchen kann.
Natürlich wird es zb eine Seite „Über uns“ und Zielgebietsinfos und noch andere Seiten geben. Primär geht es jetzt mal um das Design an sich das unser Programmierer dann sicher umsetzen kann.
Das Büro ist bisschen im Factory Style eingerichtet und wird aktuell noch mehr diesem Style angepasst.
Der Name Wander Nest spiegelt den chilligen Lifestyle wieder den wir verkörpern.

```html
<!DOCTYPE html>
<html lang="de">
<head>
<meta charset="utf-8">
<title>Wander Nest – Reisebüro</title>
<link rel="stylesheet" href="https://fonts.googleapis.com/css2?family=Alegreya:wght@700&family=Roboto:wght@400;500&display=swap">
<style>
  :root{
    --taupe:#bcaea4;
    --slate:#5a5f63;
    --slate-dark:#4f5458;
    --footer:#c3c3c3;
    --brown:#45302a;
    --white:#ffffff;
    --ink:#5a5f63;
    --heading:"Alegreya", Georgia, serif;
    --body:"Roboto", Arial, sans-serif;
  }
  *{box-sizing:border-box;margin:0;padding:0}
  html,body{width:1200px;height:3000px;overflow:hidden;background:var(--white)}
  body{font-family:var(--body);color:var(--white);position:relative}
  .page{position:absolute;left:56px;top:110px;width:1080px;height:2808px;box-shadow:0 2px 10px rgba(0,0,0,.25);overflow:hidden}

  /* navigation */
  .nav{position:absolute;left:0;top:0;width:1080px;height:54px;background:var(--taupe);z-index:3}
  .nav .social{position:absolute;left:26px;top:14px;display:flex;gap:12px}
  .nav .social span{width:26px;height:26px;border-radius:50%;background:var(--slate)}
  .nav .link{position:absolute;top:21px;font-size:10px;letter-spacing:.1em;color:var(--white);transform:translateX(-50%)}
  .nav .phone{position:absolute;right:0;top:0;width:186px;height:54px;background:var(--slate);font-size:10px;font-weight:500;letter-spacing:.1em;display:flex;align-items:center;justify-content:center}
  .brand-badge{position:absolute;left:502px;top:14px;width:76px;height:76px;border-radius:50%;background:var(--white);border:2px solid var(--taupe);display:flex;align-items:center;justify-content:center;text-align:center;font-family:var(--heading);font-weight:700;font-size:14px;line-height:1.05;color:var(--ink)}

  /* hero */
  .hero{position:absolute;left:0;top:54px;width:1080px;height:687px;background:linear-gradient(180deg,#c9c4c8 0%,#b5b0b6 22%,#5d6660 45%,#7d8488 58%,#6c7276 80%,#575c60 100%)}
  .hero h1{position:absolute;left:0;top:168px;width:1080px;text-align:center;font-family:var(--heading);font-weight:700;font-size:47px;line-height:67px;letter-spacing:.12em;color:var(--white)}
  .hero .cta{position:absolute;left:456px;top:355px;width:165px;height:42px;border:1.5px solid var(--white);border-radius:21px;font-size:11px;letter-spacing:.12em;display:flex;align-items:center;justify-content:center}

  /* about */
  .about{position:absolute;left:0;top:741px;width:1080px;height:487px;background:var(--slate)}
  .about h2{position:absolute;left:271px;top:92px;font-family:var(--heading);font-weight:700;font-size:28px;letter-spacing:.14em}
  .about p{position:absolute;left:271px;top:165px;width:255px;font-size:11px;line-height:30px;letter-spacing:.05em}
  .about .portrait{position:absolute;left:623px;top:87px;width:294px;height:306px;background:linear-gradient(160deg,#c49a7c,#a98069 45%,#7f7f86 80%,#6d6f75)}
  .about .frame{position:absolute;left:635px;top:99px;width:295px;height:306px;border:1px solid var(--white)}

  /* ship band */
  .ship{position:absolute;left:0;top:1228px;width:1080px;height:417px;background:linear-gradient(180deg,#b7c3d0 0%,#c6ccd2 38%,#5e6f55 62%,#5d7680 80%,#4e6b78 100%)}

  /* offers */
  .offers{position:absolute;left:0;top:1645px;width:1080px;height:870px;background:var(--slate)}
  .offers h2{position:absolute;left:0;top:100px;width:1080px;text-align:center;font-family:var(--heading);font-weight:700;font-size:28px;letter-spacing:.14em}
  .offers .intro{position:absolute;left:200px;top:160px;width:680px;text-align:center;font-size:11px;line-height:30px;letter-spacing:.05em}
  .card{position:absolute;top:337px;height:427px}
  .card .photo{height:332px}
  .card .caption{height:95px;background:var(--taupe);padding:14px 13px 0}
  .card h3{font-family:var(--heading);font-weight:700;font-size:27px;letter-spacing:.1em;line-height:30px}
  .card .caption p{font-size:10.5px;line-height:15px;letter-spacing:.05em;margin-top:6px;width:200px}
  .card .caption p svg{vertical-align:-1px;margin-left:4px}
  .card-hk{left:128px;width:264px}
  .card-hk .photo{background:linear-gradient(180deg,#e8d6d4 0%,#6f9a8b 35%,#2f6a62 70%,#3c4c3e 100%)}
  .card-my{left:415px;width:256px}
  .card-my .photo{background:linear-gradient(180deg,#2a3a3c 0%,#3c4a45 40%,#6a6c68 70%,#2b3032 100%)}
  .card-th{left:699px;width:250px}
  .card-th .photo{background:linear-gradient(180deg,#6aaed2 0%,#8bc0dc 45%,#50723e 75%,#d8d3c8 100%)}

  /* footer */
  .contact{position:absolute;left:0;top:2515px;width:1080px;height:244px;background:var(--footer);color:var(--ink)}
  .contact h2{font-family:var(--heading);font-weight:700;font-size:27px;letter-spacing:.1em;line-height:30px}
  .contact .col{position:absolute;top:43px;font-size:12px;line-height:18px;letter-spacing:.02em}
  .contact .address{left:128px}
  .contact .address address{font-style:normal;margin-top:6px}
  .contact .lines{margin-top:12px;list-style:none}
  .contact .lines li{display:flex;align-items:center;gap:8px;line-height:22px}
  .contact .hours{left:699px}
  .contact .hours p{margin-top:8px;line-height:14.5px}
  .contact .badge{position:absolute;left:475px;top:44px;width:146px;height:146px;border-radius:50%;background:#d6d6d6;border:3px solid var(--ink);display:flex;align-items:center;justify-content:center;text-align:center;font-family:var(--heading);font-weight:700;font-size:24px;line-height:1.05;color:var(--ink)}

  .bottom-bar{position:absolute;left:0;top:2759px;width:1080px;height:49px;background:var(--brown);font-size:12px;letter-spacing:.04em;display:flex;align-items:center;justify-content:space-between;padding:0 26px 0 33px}
</style>
</head>
<body>
<div class="page">
  <header class="nav">
    <div class="social"><span aria-label="Social-Media-Link"></span><span aria-label="Social-Media-Link"></span></div>
    <a class="link" style="left:358px">ASIA</a>
    <a class="link" style="left:438px">ÜBER UNS</a>
    <a class="link" style="left:631px">REISEN</a>
    <a class="link" style="left:712px">KONTAKT</a>
    <div class="phone">+49 - (0)800 - 123 45 60</div>
  </header>
  <div class="brand-badge">Wander<br>Nest</div>

  <section class="hero" role="img" aria-label="Frau steht im ruhigen Bergsee vor bewaldeten Hügeln unter bewölktem Himmel">
    <h1>PELLENTESQUE LOREM<br>CRAS ALIQUAM CURSUS.</h1>
    <a class="cta">ENTDECKEN</a>
  </section>

  <section class="about">
    <h2>ÜBER UNS</h2>
    <p>Fermentum, velit turpis ullamcorper tincidunt facilisis ac tempor, lectus. Ut aliquam donec libero nunc suspendisse purus, enim velit. Sit iaculis pharetra in ut faucibus nunc. At donec id eget diam. Bibendum vitae, adipiscing vel id. Praesent consectetur urna turpis nunc.</p>
    <div class="portrait" role="img" aria-label="Porträt des Inhabers vor einer Felstreppe"></div>
    <div class="frame"></div>
  </section>

  <section class="ship" role="img" aria-label="Reisegruppe auf dem Bugspriet eines Segelschiffs vor tropischer Insel"></section>

  <section class="offers">
    <h2>TOP ANGEBOTE</h2>
    <p class="intro">Amet orci neque nulla praesent a habitasse libero sed semper. Sollicitudin et gravida donec semper morbi rhoncus eget. Pharetra orci nunc molestie aliquet nec. Lorem rutrum vel fermentum leo purus eleifend dolor vivamus gravida. Eget dictumst sed arcu, ipsum, augue elit. Erat sit morbi arcu auctor.</p>

    <article class="card card-hk">
      <div class="photo" role="img" aria-label="Große Buddha-Statue in grüner Berglandschaft"></div>
      <div class="caption"><h3>HONGKONG</h3><p>Amet orci neque nulla praesent a habitasse libero sed semper.<svg width="7" height="8" viewBox="0 0 7 8"><path d="M0 0L7 4L0 8Z" fill="#fff"/></svg></p></div>
    </article>
    <article class="card card-my">
      <div class="photo" role="img" aria-label="Nächtliche Stadtansicht mit beleuchteten Zwillingstürmen"></div>
      <div class="caption"><h3>MALAYSIA</h3><p>Amet orci neque nulla praesent a habitasse libero sed semper.<svg width="7" height="8" viewBox="0 0 7 8"><path d="M0 0L7 4L0 8Z" fill="#fff"/></svg></p></div>
    </article>
    <article class="card card-th">
      <div class="photo" role="img" aria-label="Palmen an einem Sandstrand unter blauem Himmel"></div>
      <div class="caption"><h3>THAILAND</h3><p>Amet orci neque nulla praesent a habitasse libero sed semper.<svg width="7" height="8" viewBox="0 0 7 8"><path d="M0 0L7 4L0 8Z" fill="#fff"/></svg></p></div>
    </article>
  </section>

  <footer class="contact">
    <div class="col address">
      <h2>KONTAKT</h2>
      <address>Wander Nest<br>Kieselweg 7<br>86150 Lindenau</address>
      <ul class="lines">
        <li><svg width="13" height="13" viewBox="0 0 13 13"><circle cx="6.5" cy="6.5" r="6.5" fill="#5a5f63"/><path d="M4 3.5l1.3-.3.8 1.8-.9.7a4.5 4.5 0 0 0 2.1 2.1l.7-.9 1.8.8-.3 1.3c-3 .3-5.8-2.5-5.5-5.5z" fill="#c3c3c3"/></svg>+49 - (0)800 - 123 45 60</li>
        <li><svg width="13" height="13" viewBox="0 0 13 13"><circle cx="6.5" cy="6.5" r="6.5" fill="#5a5f63"/><rect x="3.5" y="5" width="6" height="4" fill="#c3c3c3"/><rect x="4.5" y="3" width="4" height="2" fill="#c3c3c3"/></svg>+49 - (0)800 - 123 45 67</li>
        <li><svg width="13" height="13" viewBox="0 0 13 13"><circle cx="6.5" cy="6.5" r="6.5" fill="#5a5f63"/><circle cx="6.5" cy="6.5" r="3" fill="none" stroke="#c3c3c3" stroke-width="1.3"/></svg>info@wandernest-reisen.de</li>
      </ul>
    </div>
    <div class="badge">Wander<br>Nest</div>
    <div class="col hours">
      <h2>ÖFFNUNGSZEITEN</h2>
      <p>Montag - Freitag<br>10.00 - 13.00 Uhr<br>14.00 - 18.00 Uhr<br>Mittwoch Vormittag geschlossen</p>
      <p style="margin-top:14px">Samstag<br>10.00 - 13.00 Uhr</p>
    </div>
  </footer>

  <div class="bottom-bar"><span>WANDER NEST • 2020</span><span>DATENSCHUTZ • IMPRESSUM</span></div>
</div>
</body>
</html>
```